Business Card Design

This is a coaching and training company. We deliver personal development workshops, training and one to one coaching. We would like the current logo to be used.

Target Market(s)

For coaches, small business owners and people aged around 40-60 who are seeking direction in their life

Industry/Entity Type

Training

Contact Information for Business Card

Moira Treadwell
Speaker-Trainer-Coach
There is no going back ...
0461 839205
18 Pellow Road Marbury
motread47@quillnet.example

Font styles to use
Sans Serif

Requirements
Should not have
• No old style fonts

```html
<!DOCTYPE html>
<html lang="en">
<head>
<meta charset="utf-8">
<title>Crossway Coaching and Training Solutions – Business Card</title>
<link rel="stylesheet" href="https://fonts.googleapis.com/css2?family=Source+Sans+3:wght@400;600&display=swap">
<style>
  :root {
    --page: #e9ebed;
    --card-white: #ffffff;
    --brand-blue: #3aa9da;
    --band-teal: #1f6f8e;
    --band-teal-dark: #185a74;
    --logo-blue: #2f8fc4;
    --logo-grey: #dcdee0;
    --text-grey: #6b6f73;
    --text-white: #ffffff;
    --shadow: rgba(30, 40, 50, 0.18);
  }
  * { box-sizing: border-box; margin: 0; padding: 0; }
  html, body {
    width: 1200px; height: 872px; overflow: hidden;
    background: var(--page);
  }
  .sheet {
    width: 1200px; height: 872px;
    display: flex; align-items: center; justify-content: center; gap: 40px;
  }
  .card {
    position: relative;
    width: 540px; height: 310px;
    background: var(--card-white);
    overflow: hidden;
    box-shadow: 0 6px 18px var(--shadow);
    font-family: "Source Sans 3", sans-serif;
  }

  /* ---------- Front ---------- */
  .front__blue {
    position: absolute; top: 0; right: 0; bottom: 0; width: 49%;
    background: var(--brand-blue);
  }
  .front__white-tab {
    position: absolute; top: 0; right: 0; width: 49%; height: 34px;
    background: var(--card-white);
  }
  .front__mark {
    position: absolute; left: 92px; top: 40px;
    width: 120px; height: 120px;
    background: linear-gradient(135deg, #f1f2f3, var(--logo-grey));
  }
  .front__company {
    position: absolute; left: 22px; top: 170px; width: 260px;
    text-align: center;
  }
  .company-name {
    color: var(--logo-blue);
    font-size: 40px; font-weight: 400; letter-spacing: 2px; line-height: 1;
    text-transform: uppercase;
  }
  .company-sub {
    margin-top: 6px;
    color: var(--text-grey);
    font-size: 13px; letter-spacing: 0.3px;
  }
  .name-band {
    position: absolute; top: 34px; right: 0; width: 51%; height: 70px;
    background: var(--band-teal);
    padding: 12px 20px 0 22px;
    color: var(--text-white);
    white-space: nowrap;
  }
  .name-band::before {
    content: ""; position: absolute; left: -14px; top: 0;
    border-top: 70px solid var(--band-teal-dark);
    border-left: 14px solid transparent;
  }
  .person-name {
    font-size: 22px; font-weight: 600; letter-spacing: 1.5px; line-height: 1.1;
    text-transform: uppercase;
  }
  .person-role {
    margin-top: 7px; font-size: 11px; letter-spacing: 1.2px;
    text-transform: uppercase;
  }
  .contacts {
    position: absolute; left: 57%; top: 136px; right: 12px;
    list-style: none; color: var(--text-white);
  }
  .contacts li {
    display: flex; align-items: center; gap: 12px;
    font-size: 14px; letter-spacing: 0.4px; margin-bottom: 18px;
    white-space: nowrap;
  }
  .contacts svg { width: 16px; height: 16px; flex: none; }

  /* ---------- Back ---------- */
  .back__blue {
    position: absolute; top: 0; left: 0; bottom: 0; width: 216px;
    background: var(--brand-blue);
  }
  .back__blue-top {
    position: absolute; top: 0; left: 0; right: 0; height: 40px;
    background: var(--brand-blue);
  }
  .back__logo-box {
    position: absolute; left: 150px; top: 40px;
    width: 130px; height: 120px;
    background: var(--card-white);
    display: flex; flex-direction: column; align-items: center; justify-content: center;
  }
  .back__logo-box .square {
    width: 48px; height: 48px; margin-bottom: 8px;
    background: linear-gradient(135deg, #f1f2f3, var(--logo-grey));
  }
  .back__logo-box .company-name { font-size: 20px; letter-spacing: 1px; }
  .back__logo-box .company-sub { font-size: 7px; margin-top: 3px; }
  .tagline {
    position: absolute; left: 0; right: 0; bottom: 24px;
    font-size: 18px; letter-spacing: 2px; text-transform: uppercase;
    line-height: 1;
  }
  .tagline__lead {
    position: absolute; right: calc(100% - 216px); bottom: 0;
    padding-right: 8px; white-space: nowrap;
    color: var(--text-white);
  }
  .tagline__tail {
    position: absolute; left: 222px; bottom: 0;
    white-space: nowrap;
    color: var(--brand-blue);
  }
</style>
</head>
<body>
<main class="sheet">

  <section class="card card--front" aria-label="Business card front">
    <div class="front__blue"></div>
    <div class="front__white-tab"></div>
    <div class="front__mark" aria-hidden="true"></div>
    <div class="front__company">
      <div class="company-name">Crossway</div>
      <div class="company-sub">Coaching and Training Solutions</div>
    </div>
    <div class="name-band">
      <div class="person-name">Moira Treadwell</div>
      <div class="person-role">Speaker-Trainer-Coach</div>
    </div>
    <ul class="contacts">
      <li>
        <svg viewBox="0 0 16 16" aria-hidden="true"><rect x="4" y="1" width="8" height="14" rx="1.5" fill="none" stroke="#fff" stroke-width="1.5"/><circle cx="8" cy="12.5" r="0.9" fill="#fff"/></svg>
        0461 839205
      </li>
      <li>
        <svg viewBox="0 0 16 16" aria-hidden="true"><path d="M8 15s-5-5.2-5-8.6A5 5 0 0 1 13 6.4C13 9.8 8 15 8 15z" fill="none" stroke="#fff" stroke-width="1.5"/><circle cx="8" cy="6.4" r="1.7" fill="#fff"/></svg>
        18 Pellow Road Marbury
      </li>
      <li>
        <svg viewBox="0 0 16 16" aria-hidden="true"><rect x="1" y="3" width="14" height="10" fill="none" stroke="#fff" stroke-width="1.5"/><path d="M1 3l7 6 7-6" fill="none" stroke="#fff" stroke-width="1.5"/></svg>
        motread47@quillnet.example
      </li>
    </ul>
  </section>

  <section class="card card--back" aria-label="Business card back">
    <div class="back__blue"></div>
    <div class="back__blue-top"></div>
    <div class="back__logo-box">
      <div class="square" aria-hidden="true"></div>
      <div class="company-name">Crossway</div>
      <div class="company-sub">Coaching and Training Solutions</div>
    </div>
    <p class="tagline"><span class="tagline__lead">There is no going</span><span class="tagline__tail">back.....</span></p>
  </section>

</main>
</body>
</html>
```